New business card for my lawn and landscape business

Dorrin Yard and Building is a full-service lawn care, landscaping, and light construction company serving Paragould and the Northeast Arkansas region. The business is owned and operated by Marcus Toller, with a reputation for hands-on, detail-oriented service, dependable crews, and quality results for both residential and commercial clients. A well regarded business with great reviews.
Owner Marcus Toller
Dorrinyardandbuilding.example

Target Market(s)

Commercial, Middle, and upper class in north east Arkansas

Industry/Entity Type

Lawn maintenance and landscape

Contact Information for Business Card

Dorrin Yard And Building Professional lawn care, landscaping, and property improvement in Northeast Arkansas. • lawn maintenance •lawn treatments and weed control • exterior projects • Custom landscape design & installation • Sod, trees, rock & drainage solutions • Residential & commercial services Reliable. Detailed. Done right.

Requirements
Must have
• Business name, service area, list of some of our services, clean design that represents
Nice to have
• Unique. Different design element than just grass because its already in n the logo. Picture of a warm season (south) lawn or landscape. Pictures of the type of work we do

```html
<!DOCTYPE html>
<html lang="en">
<head>
<meta charset="utf-8">
<title>Dorrin Yard and Building – Business Card</title>
<link rel="stylesheet" href="https://fonts.googleapis.com/css2?family=Montserrat:wght@400;500;700&family=Oswald:wght@500;600&display=swap">
<style>
  :root {
    --green: #7cb32b;
    --black: #1c1c1c;
    --white: #ffffff;
    --ink: #1a1a1a;
    --grey: #8a8a8a;
    --backdrop: #e9e9e9;
  }
  * { box-sizing: border-box; margin: 0; padding: 0; }
  html, body {
    width: 1200px; height: 1200px; overflow: hidden;
    background: var(--backdrop);
    font-family: "Montserrat", sans-serif;
  }
  .canvas { position: relative; width: 1200px; height: 1200px; }
  .card {
    position: absolute; left: 150px; width: 900px; height: 514px;
    border-radius: 34px; overflow: hidden;
    box-shadow: 0 6px 18px rgba(0,0,0,.18);
  }
  .card--front { top: 62px; background: var(--white); }
  .card--back { top: 624px; background: var(--black); border: 3px solid var(--green); }

  .front-bands { position: absolute; inset: 0; width: 900px; height: 514px; }

  .holder { position: absolute; left: 62px; top: 128px; }
  .holder__name { color: var(--green); font-weight: 700; font-size: 38px; letter-spacing: .5px; line-height: 1; }
  .holder__role { color: var(--ink); font-size: 20px; font-weight: 500; margin-top: 4px; }

  .contacts { position: absolute; left: 62px; top: 200px; list-style: none; }
  .contacts li { display: flex; align-items: flex-start; gap: 12px; font-size: 17px; color: var(--ink); line-height: 1.2; margin-bottom: 4px; }
  .contacts svg { width: 18px; height: 18px; flex: none; margin-top: 1px; fill: var(--green); }

  .brand {
    position: absolute; display: flex; align-items: center; gap: 14px;
    font-family: "Montserrat", sans-serif; font-weight: 700; color: var(--green);
  }
  .brand__dot { border-radius: 50%; background: var(--green); flex: none; }
  .brand--front { left: 470px; top: 96px; font-size: 30px; line-height: 1.1; }
  .brand--front .brand__dot { width: 26px; height: 26px; }
  .brand--back { left: 0; right: 0; top: 170px; justify-content: center; font-size: 46px; }
  .brand--back .brand__dot { width: 38px; height: 38px; }

  .services {
    position: absolute; left: 150px; right: 36px; top: 352px;
    font-family: "Oswald", sans-serif; font-weight: 600; text-transform: uppercase;
    font-size: 14.5px; color: var(--ink); line-height: 1.45; letter-spacing: .1px;
  }
  .services .sep { color: var(--green); padding: 0 4px; }
  .services__tagline { color: var(--green); font-weight: 500; font-size: 16px; }

  .back-tagline {
    position: absolute; left: 0; right: 0; top: 360px; text-align: center;
    color: var(--white); font-weight: 500; text-transform: uppercase;
    font-size: 21px; line-height: 1.3; letter-spacing: .3px;
  }
</style>
</head>
<body>
<main class="canvas">

  <section class="card card--front" aria-label="Card front">
    <svg class="front-bands" viewBox="0 0 900 514" aria-hidden="true">
      <polygon points="0,488 540,488 556,430 575,430 560,488 900,488 900,514 0,514" fill="#7cb32b"/>
      <polygon points="588,430 900,430 900,488 573,488" fill="#1c1c1c"/>
    </svg>

    <div class="brand brand--front"><span class="brand__dot"></span><span>Dorrin Yard<br>and Building</span></div>

    <div class="holder">
      <div class="holder__name">MARCUS TOLLER</div>
      <div class="holder__role">OWNER</div>
    </div>

    <ul class="contacts">
      <li>
        <svg viewBox="0 0 24 24"><path d="M6.6 10.8a15.2 15.2 0 0 0 6.6 6.6l2.2-2.2a1 1 0 0 1 1-.25 11.4 11.4 0 0 0 3.6.57 1 1 0 0 1 1 1V20a1 1 0 0 1-1 1A17 17 0 0 1 3 4a1 1 0 0 1 1-1h3.5a1 1 0 0 1 1 1c0 1.25.2 2.46.57 3.6a1 1 0 0 1-.25 1z"/></svg>
        <span>(000) 000 0000</span>
      </li>
      <li>
        <svg viewBox="0 0 24 24"><path d="M2 5h20v14H2z M2 5l10 8 10-8" fill="none" stroke="#7cb32b" stroke-width="2.4"/></svg>
        <span>email@company.com</span>
      </li>
      <li>
        <svg viewBox="0 0 24 24"><circle cx="12" cy="12" r="9.5" fill="none" stroke="#7cb32b" stroke-width="2"/><path d="M2.5 12h19M12 2.5c3 3 3 16 0 19M12 2.5c-3 3-3 16 0 19" fill="none" stroke="#7cb32b" stroke-width="1.6"/></svg>
        <span>www.company.com</span>
      </li>
      <li>
        <svg viewBox="0 0 24 24"><path d="M12 2a7 7 0 0 0-7 7c0 5 7 13 7 13s7-8 7-13a7 7 0 0 0-7-7zm0 9.5A2.5 2.5 0 1 1 12 6.5a2.5 2.5 0 0 1 0 5z"/></svg>
        <span>123 Name Street, 000<br>Your City, 00000-000</span>
      </li>
    </ul>

    <div class="services">
      <div><span class="sep">•</span>Lawn Maintenance <span class="sep">•</span>Lawn Treatments and Weed Control <span class="sep">•</span>Exterior Projects <span class="sep">•</span>Custom Landscape</div>
      <div>Design &amp; Installation <span class="sep">•</span>Sod, Trees, Rock &amp; Drainage Solutions <span class="sep">•</span>Residential &amp; Commercial Services</div>
      <div class="services__tagline">Services Reliable. Detailed. Done Right.</div>
    </div>
  </section>

  <section class="card card--back" aria-label="Card back">
    <div class="brand brand--back"><span class="brand__dot"></span><span>Dorrin Yard and Building</span></div>
    <p class="back-tagline">Professional lawn care, landscaping, and property<br>improvement in Northeast Arkansas.</p>
  </section>

</main>
</body>
</html>
```